" Empresa em abertura de firma (status), voltada para o segmento de Headhunter / Jobhunter, Coaching e demais serviços administrativos/treinamento relacionados. "

```html
<!DOCTYPE html>
<html lang="pt">
<head>
<meta charset="utf-8">
<title>PrimeStaff – Banner</title>
<link href="https://fonts.googleapis.com/css2?family=Open+Sans:wght@400;600&display=swap" rel="stylesheet">
<style>
  :root {
    --page-bg: #eef0f3;
    --card-white: #ffffff;
    --blue-light: #b9d3ef;
    --blue-mid: #7fa9e0;
    --blue-deep: #3f7fd0;
    --brand-blue: #2e5fa8;
    --text-light: #ffffff;
    --mark-tint: rgba(255,255,255,0.22);
  }
  html, body {
    margin: 0;
    width: 1200px;
    height: 1200px;
    overflow: hidden;
    background: var(--page-bg);
    font-family: "Open Sans", Arial, sans-serif;
  }
  .banner {
    position: absolute;
    left: 379px;
    top: 58px;
    width: 442px;
    height: 1085px;
    border-radius: 34px;
    overflow: hidden;
    background: var(--card-white);
    box-shadow: 0 6px 24px rgba(0,0,0,0.12);
  }
  .banner-bg {
    position: absolute;
    inset: 0;
    width: 100%;
    height: 100%;
  }
  .brand {
    position: absolute;
    left: 0;
    right: 0;
    top: 150px;
    text-align: center;
  }
  .brand-mark {
    width: 150px;
    height: 150px;
    margin: 0 auto 34px;
    border-radius: 50%;
    background: var(--brand-blue);
  }
  .brand-name {
    margin: 0;
    font-size: 50px;
    font-weight: 600;
    letter-spacing: -1px;
    color: var(--brand-blue);
  }
  .contacts {
    position: absolute;
    left: 44px;
    top: 560px;
    color: var(--text-light);
  }
  .contact-row {
    display: flex;
    align-items: flex-start;
    gap: 22px;
    margin-bottom: 28px;
  }
  .contact-icon {
    width: 36px;
    height: 36px;
    flex: none;
    margin-top: 4px;
  }
  .contact-text {
    font-size: 29px;
    line-height: 42px;
    font-weight: 400;
  }
  .contact-text.handle { font-weight: 600; }
  .faint-mark {
    position: absolute;
    left: 141px;
    top: 820px;
    width: 160px;
    height: 160px;
    border-radius: 50%;
    background: var(--mark-tint);
  }
</style>
</head>
<body>
  <div class="banner">
    <svg class="banner-bg" viewBox="0 0 442 1085" preserveAspectRatio="none" aria-hidden="true">
      <defs>
        <linearGradient id="blueFill" x1="0" y1="0" x2="0" y2="1">
          <stop offset="0" stop-color="var(--blue-light)"/>
          <stop offset="0.45" stop-color="var(--blue-mid)"/>
          <stop offset="1" stop-color="var(--blue-deep)"/>
        </linearGradient>
      </defs>
      <path d="M0 500 C 90 455, 170 520, 260 505 C 340 492, 400 450, 442 470 L442 1085 L0 1085 Z" fill="url(#blueFill)"/>
      <path d="M0 960 C 120 1010, 300 1030, 442 1000 L442 1030 C 300 1060, 130 1045, 0 1000 Z" fill="#ffffff" opacity="0.95"/>
    </svg>

    <div class="brand">
      <div class="brand-mark"></div>
      <p class="brand-name">PrimeStaff</p>
    </div>

    <div class="contacts">
      <div class="contact-row">
        <svg class="contact-icon" viewBox="0 0 24 24" aria-label="Telefone">
          <path fill="#ffffff" d="M6.6 10.8a15.1 15.1 0 0 0 6.6 6.6l2.2-2.2a1 1 0 0 1 1-.25 11.4 11.4 0 0 0 3.6.57 1 1 0 0 1 1 1V20a1 1 0 0 1-1 1A17 17 0 0 1 3 4a1 1 0 0 1 1-1h3.5a1 1 0 0 1 1 1c0 1.25.2 2.45.57 3.57a1 1 0 0 1-.25 1z"/>
        </svg>
        <div class="contact-text">00 0000-0000<br>00 0000-0000</div>
      </div>
      <div class="contact-row">
        <svg class="contact-icon" viewBox="0 0 24 24" aria-label="Web">
          <g fill="none" stroke="#ffffff" stroke-width="1.6">
            <circle cx="12" cy="12" r="9.5"/>
            <ellipse cx="12" cy="12" rx="4.2" ry="9.5"/>
            <path d="M2.5 12h19M4 7h16M4 17h16"/>
          </g>
        </svg>
        <div class="contact-text handle">@primestaffhq</div>
      </div>
    </div>

    <div class="faint-mark"></div>
  </div>
</body>
</html>
```